Publisher needs a book cover design for ‘Lanterns Over the Marsh Gate’ book

We need a book cover (front, back, spine) for the 2nd edition of a book entitled ‘Lanterns Over the Marsh Gate’ and subtitled ‘the quiet geography of tidal winds, ferry routes and harbour lanterns’ (inverted commas not to be part of the title and subtitle). The author is Rupert Calloway. The publisher is Vellmark Press. The finished size of the paperback version will be the industry standard 9" x 6". There will be paperback, hardback, and e-book versions. The final number of pages is expected to be in the region 150-180 pages. Text for the back cover is not yet available, but at the bottom of the back cover should be publisher logo (rectangular) on the left and space for the ISBN bar code on the right. The circular logo should be on the spine. The design should be original and not include any stock images that have been created by someone else or may require obtaining a copyright licence to use. Symbols in common use and not copyrighted are probably ok. There are no required images, photographs or symbols except the publisher logo at the left bottom of the back cover and lower spine. Spine lettering should be UK/US style with the top of the writing nearest the front cover. The designer is free to be creative using appropriate diagrams, symbols or abstract designs. Rectangular and circular variants of the publisher logo are attached. Designers are assured that when evaluating designs absolutely no notice whatsoever is taken of a designer's Pixo Rally ranking or status; We are completely output driven, so what matters is the design, not the ranking or status of the designer. In a similar way, designs are not evaluated as 'good' or 'bad' - the winning design will be chosen after review by a design review panel and is not decided arbitrarily by a single person. All submitted designs should be capable of effective copyright assignment.

Target Market(s)

Practitioners, parents, teachers, pupils and academics concerned with child protection, safeguarding and the elimination of emotional abuse of children in the classroom

Font styles to use
Serif
Sans Serif

Requirements
Must have
• • Title, author, edition, subtitle, publisher logo
Nice to have
• • Originality, innovation
Should not have
• • Stock images or anything else requiring additional copyright discussions and negotiations.

```html
<!DOCTYPE html>
<html lang="en">
<head>
<meta charset="utf-8">
<title>Lanterns Over the Marsh Gate — Cover</title>
<link rel="stylesheet" href="https://fonts.googleapis.com/css2?family=Tinos:wght@400;700&family=Roboto:wght@400;500;700&family=Roboto+Condensed:wght@500&family=Open+Sans:wght@400;700&family=Cinzel&display=swap">
<style>
  :root {
    --paper: #ffffff;
    --ink: #000000;
    --eye-light: #e9e9e9;
    --eye-mid: #9a9a9a;
    --room-top: #d9d6c6;
    --room-mid: #a8a8ae;
    --room-desk: #a88862;
    --room-dark: #3c4350;
  }
  html, body { margin: 0; padding: 0; overflow: hidden; background: var(--paper); }
  .cover {
    position: relative;
    width: 1200px; height: 845px;
    background: var(--paper);
    overflow: hidden;
    color: var(--ink);
  }
  .back-illustration {
    position: absolute; left: 120px; top: 0; width: 276px; height: 196px;
    border-radius: 50%;
    background: radial-gradient(ellipse at 50% 45%, var(--eye-mid) 0%, #c4c4c4 35%, var(--eye-light) 65%, rgba(255,255,255,0) 72%);
  }
  .back-publisher {
    position: absolute; left: 40px; top: 750px;
    display: flex; align-items: center; gap: 8px;
  }
  .back-publisher .mark {
    width: 46px; height: 46px; border-radius: 50%; background: var(--ink);
  }
  .back-publisher .name {
    font-family: "Cinzel", serif; font-size: 24px; letter-spacing: 0.5px;
  }
  .spine {
    position: absolute; left: 560px; top: 0; width: 60px; height: 845px;
  }
  .spine-text {
    position: absolute; left: 44px; top: 22px;
    transform-origin: 0 0; transform: rotate(90deg);
    white-space: nowrap; display: flex; align-items: baseline; gap: 22px;
  }
  .spine-title { font-family: "Roboto", sans-serif; font-weight: 700; font-size: 30px; }
  .spine-author { font-family: "Roboto", sans-serif; font-weight: 400; font-size: 25px; }
  .spine-publisher {
    position: absolute; left: 556px; top: 780px; width: 68px;
    display: flex; flex-direction: column; align-items: center; gap: 3px;
  }
  .spine-publisher .mark { width: 38px; height: 38px; border-radius: 50%; background: var(--ink); }
  .spine-publisher .name { font-family: "Cinzel", serif; font-size: 8px; }
  .front-illustration {
    position: absolute; left: 641px; top: 0; width: 559px; height: 282px;
    background: linear-gradient(180deg, var(--room-top) 0%, var(--room-top) 14%, var(--room-mid) 20%, var(--room-desk) 45%, var(--room-dark) 60%, var(--room-desk) 78%, var(--room-dark) 100%);
  }
  .front-rule {
    position: absolute; left: 670px; top: 312px; width: 1px; height: 272px; background: var(--ink);
  }
  .front-title {
    position: absolute; left: 718px; top: 298px; margin: 0;
    font-family: "Tinos", serif; font-weight: 400; font-size: 72px; line-height: 101px;
    letter-spacing: 1px;
  }
  .front-subtitle {
    position: absolute; left: 719px; top: 610px; width: 440px; margin: 0;
    font-family: "Open Sans", sans-serif; font-size: 20px; line-height: 30px;
  }
  .front-edition {
    position: absolute; left: 719px; top: 694px; margin: 0;
    font-family: "Roboto Condensed", sans-serif; font-weight: 500; font-size: 24px;
  }
  .front-author {
    position: absolute; left: 719px; top: 774px; margin: 0;
    font-family: "Open Sans", sans-serif; font-weight: 700; font-size: 28px; letter-spacing: 1.5px;
  }
</style>
</head>
<body>
<div class="cover">
  <section class="back">
    <div class="back-illustration" role="img" aria-label="Pencil drawing of a tearful eye"></div>
    <div class="back-publisher"><span class="mark"></span><span class="name">VELLMARK PRESS</span></div>
  </section>

  <section class="spine">
    <div class="spine-text">
      <span class="spine-title">Lanterns Over the Marsh Gate</span>
      <span class="spine-author">Rupert Calloway</span>
    </div>
  </section>
  <div class="spine-publisher"><span class="mark"></span><span class="name">VELLMARK</span></div>

  <section class="front">
    <div class="front-illustration" role="img" aria-label="Painted view of rows of empty desks in a room"></div>
    <div class="front-rule"></div>
    <h1 class="front-title">Lanterns<br>Over the<br>Marsh Gate</h1>
    <p class="front-subtitle">the quiet geography of tidal winds, ferry routes and harbour lanterns</p>
    <p class="front-edition">2nd EDITION</p>
    <p class="front-author">Rupert Calloway</p>
  </section>
</div>
</body>
</html>
```